Contemporary Media Company with Logo Needs Business Card Design

Need a modern card design for a full service digital media company using the logo included. Also want the info below on the card. Probably list the services on the card back to save space for the front. Want something contemporary to impress prospective clients. You may want to submit both a somewhat more conservative design, and then a more wild one.
General Info: (this phrase need not be on the card)
Tod Parvin
Founder and CEO
949-628-4513
tod@lumavantstudio.example
lumavantstudio.example
Services: (this word need not be on the card)
Content & Experience Strategy
Brand Development
Search Engine Optimization
Website Design
Website Operation
Social Media Integration
Complete Video Solutions
Industry/Entity Type
Business
Contact Information for Business Card
Tod Parvin
Founder and CEO
949-628-4513
tod@lumavantstudio.example
lumavantstudio.example
Brand Development
Website Design
Website Operation
Social Media Integration
Complete Video Solutions
Look and feel

```html
<!DOCTYPE html>
<html lang="en">
<head>
<meta charset="utf-8">
<title>Lumavant Studio — Business Card</title>
<link rel="stylesheet" href="https://fonts.googleapis.com/css2?family=Courier+Prime:wght@400;700&display=swap">
<style>
  :root {
    --page: #ffffff;
    --card: #ffffff;
    --frame: #231f20;
    --orange: #f07a2a;
    --orange-soft: #f3a06a;
    --grey: #6d6e70;
    --pattern-dark: #555557;
    --pattern-peach: #f0b892;
    --pattern-faint: #f2f2f2;
  }
  * { margin: 0; padding: 0; box-sizing: border-box; }
  html, body {
    width: 1200px;
    height: 960px;
    overflow: hidden;
    background: var(--page);
  }
  body {
    position: relative;
    font-family: "Courier Prime", "Courier New", monospace;
  }
  .card {
    position: absolute;
    left: 259px;
    width: 428px;
    height: 237px;
    background: var(--card);
    border: 2px solid var(--frame);
    overflow: hidden;
  }
  .card--front { top: 94px; }
  .card--back { top: 443px; }

  .card__pattern {
    position: absolute;
    left: 0;
    top: 0;
    width: 424px;
    height: 233px;
  }
  .pattern-stop--dark { stop-color: var(--pattern-dark); }
  .pattern-stop--peach { stop-color: var(--pattern-peach); }
  .pattern-shape--faint { fill: var(--pattern-faint); }

  .identity {
    position: absolute;
    right: 11px;
    top: 6px;
    text-align: right;
    color: var(--orange);
    font-weight: 700;
    font-size: 11.5px;
    line-height: 14px;
  }

  .brand {
    position: absolute;
    left: 12px;
    top: 204px;
    display: flex;
    align-items: center;
    gap: 6px;
  }
  .brand__mark {
    width: 12px;
    height: 12px;
    background: var(--orange);
  }
  .brand__name {
    color: var(--grey);
    font-size: 9px;
    font-weight: 700;
    letter-spacing: 0.6px;
  }

  .contact {
    position: absolute;
    left: 281px;
    top: 194px;
    list-style: none;
    color: var(--orange-soft);
    font-size: 7.5px;
    line-height: 11.5px;
    white-space: nowrap;
  }
  .contact__item {
    display: flex;
    align-items: center;
    gap: 1px;
  }
  .contact__icon {
    width: 10px;
    height: 10px;
    flex: none;
  }

  .services {
    position: absolute;
    left: 0;
    right: 0;
    top: 36px;
    list-style: none;
    text-align: center;
    color: var(--orange-soft);
    font-size: 10px;
    line-height: 24px;
  }
</style>
</head>
<body>

<section class="card card--front">
  <svg class="card__pattern" viewBox="0 0 424 233" role="img" aria-label="Large geometric pattern of interlocking triangles with a marbled grey and peach texture">
    <defs>
      <linearGradient id="front-pattern-fill" x1="0" y1="0" x2="1" y2="1">
        <stop offset="0" class="pattern-stop--dark"/>
        <stop offset="0.35" class="pattern-stop--peach"/>
        <stop offset="0.55" class="pattern-stop--dark"/>
        <stop offset="0.8" class="pattern-stop--peach"/>
        <stop offset="1" class="pattern-stop--dark"/>
      </linearGradient>
    </defs>
    <polygon points="193,0 221,0 318,70 348,117 318,162 221,232 193,232 97,162 77,117 97,70" fill="url(#front-pattern-fill)" opacity="0.85"/>
  </svg>

  <div class="identity">
    <p class="identity__name">Tod Parvin</p>
    <p class="identity__title">Founder and CEO</p>
  </div>

  <div class="brand">
    <span class="brand__mark"></span>
    <span class="brand__name">LUMAVANT STUDIO</span>
  </div>

  <ul class="contact">
    <li class="contact__item">
      <svg class="contact__icon" viewBox="0 0 10 10" aria-hidden="true">
        <rect x="3" y="1.5" width="4" height="8" rx="1" fill="none" stroke="#f07a2a" stroke-width="1"/>
        <line x1="6.5" y1="0" x2="6.5" y2="1.5" stroke="#f07a2a" stroke-width="1"/>
        <rect x="4" y="3" width="2" height="1.5" fill="#f07a2a"/>
      </svg>:949-628-4513
    </li>
    <li class="contact__item">
      <svg class="contact__icon" viewBox="0 0 10 10" aria-hidden="true">
        <circle cx="5" cy="5" r="1.6" fill="none" stroke="#f07a2a" stroke-width="1.1"/>
        <path d="M6.6 3.4 V6 q0 1 1 1 q1.4 0 1.4-2 A4 4 0 1 0 7 8.6" fill="none" stroke="#f07a2a" stroke-width="1.1"/>
      </svg>:tod@lumavantstudio.example
    </li>
    <li class="contact__item">
      <svg class="contact__icon" viewBox="0 0 10 10" aria-hidden="true">
        <circle cx="5" cy="5" r="4.2" fill="none" stroke="#f07a2a" stroke-width="0.9"/>
        <ellipse cx="5" cy="5" rx="1.8" ry="4.2" fill="none" stroke="#f07a2a" stroke-width="0.7"/>
        <line x1="0.8" y1="5" x2="9.2" y2="5" stroke="#f07a2a" stroke-width="0.7"/>
      </svg>:lumavantstudio.example
    </li>
  </ul>
</section>

<section class="card card--back">
  <svg class="card__pattern" viewBox="0 0 424 233" role="img" aria-label="Faint light grey geometric triangle pattern behind the services list">
    <polygon class="pattern-shape--faint" points="193,0 221,0 318,70 348,117 318,162 221,232 193,232 97,162 77,117 97,70"/>
  </svg>
  <ul class="services">
    <li>Content &amp; Experience Strategy</li>
    <li>Brand Development</li>
    <li>Search Engine Optimization</li>
    <li>Website Design</li>
    <li>Website Operation</li>
    <li>Social Media Integration</li>
    <li>Complete Video Solutions</li>
  </ul>
</section>

</body>
</html>
```